Tavrin Telecom Corporate Website & Social Branding

We are looking for a new website for our startup telecom which provides UCaaS, SD-WAN, Business SMS/MMS, Video Conferencing, Managed Network Service & more.

Target Market(s)

Small offices from 1-250 users

Industry/Entity Type

Telecomunications

Coding

Coded - Design and coding required

Colors
0054AA
0677BA
7BADD7
CADEEF
E8F1F8

```html
<!DOCTYPE html>
<html lang="en">
<head>
<meta charset="utf-8">
<title>Tavrin Telecom</title>
<link href="https://fonts.googleapis.com/css2?family=Roboto:wght@400;500;700&display=swap" rel="stylesheet">
<style>
:root{
  --blue-deep:#0054AA;
  --blue:#0677BA;
  --blue-mid:#7BADD7;
  --blue-light:#CADEEF;
  --blue-pale:#E8F1F8;
  --ink:#111111;
  --text:#555b63;
  --white:#ffffff;
  --star:#f5a623;
}
*{box-sizing:border-box;margin:0;padding:0}
html,body{width:1200px;height:4494px;overflow:hidden}
body{font-family:'Roboto',sans-serif;color:var(--ink);background:var(--white);position:relative}
.abs{position:absolute}
a{color:inherit;text-decoration:none}

.topbar{position:absolute;top:0;left:0;width:1200px;height:35px;background:#f3f4f6;font-size:13px;color:#444}
.topbar span{position:absolute;top:9px}
.nav{position:absolute;top:35px;left:0;width:1200px;height:78px;background:var(--white)}
.brand{position:absolute;left:112px;top:22px;display:flex;align-items:center;gap:10px;font-size:26px;font-weight:700;color:var(--blue-deep)}
.brand i{width:30px;height:30px;border-radius:50%;background:var(--blue-deep);display:block}
.menu{position:absolute;left:410px;top:30px;display:flex;gap:27px;font-size:15px;font-weight:500}
.menu .active{color:var(--blue)}
.btn{display:inline-flex;align-items:center;justify-content:center;gap:8px;background:var(--blue-deep);color:var(--white);border-radius:24px;font-weight:500;font-size:15px}
.btn-nav{position:absolute;left:957px;top:20px;width:131px;height:38px}
.btn .dot{width:14px;height:14px;border-radius:50%;background:var(--white);position:relative}
.btn .dot:after{content:"";position:absolute;left:4px;top:4px;width:4px;height:4px;border-top:2px solid var(--blue-deep);border-right:2px solid var(--blue-deep);transform:rotate(45deg)}

.hero{position:absolute;top:113px;left:0;width:1200px;height:604px}
.hero h1{position:absolute;left:111px;top:122px;font-size:38px;font-weight:500;line-height:44px;color:var(--ink)}
.hero p{position:absolute;left:111px;top:230px;width:500px;font-size:16px;line-height:26px;color:#222}
.hero .btn{position:absolute;left:111px;top:310px;width:200px;height:48px;font-size:16px}

.h2{position:absolute;left:0;width:1200px;text-align:center;font-size:38px;font-weight:500}

.svc{position:absolute;width:470px;height:150px}
.svc .ic{position:absolute;left:0;top:0;width:90px;height:90px;border-radius:50%;background:var(--blue-deep)}
.svc h3{position:absolute;left:116px;top:0;font-size:18px;font-weight:500}
.svc p{position:absolute;left:116px;top:30px;width:350px;font-size:14px;line-height:24px;color:var(--text);text-align:justify}
.more{position:absolute;left:116px;top:116px;font-size:14px;font-weight:700;color:var(--blue-deep);display:flex;align-items:center;gap:7px}
.more i{width:13px;height:13px;border-radius:50%;background:var(--blue-deep);display:block;position:relative}
.more i:after{content:"";position:absolute;left:3px;top:4px;width:3px;height:3px;border-top:1.5px solid #fff;border-right:1.5px solid #fff;transform:rotate(45deg)}

.about-txt{position:absolute;left:672px;top:1560px;width:418px}
.about-txt h2{font-size:38px;font-weight:500;text-align:center;margin-bottom:22px}
.about-txt p{font-size:14px;line-height:26px;color:var(--text);margin-bottom:14px}
.about-txt .btn{width:186px;height:46px;margin-top:14px}

.why{position:absolute;top:2166px;width:230px;height:267px;background:var(--white);box-shadow:0 2px 12px rgba(0,0,0,.16);text-align:center}
.why svg{margin-top:26px}
.why h3{font-size:18px;font-weight:500;margin-top:12px}
.why p{font-size:14px;line-height:24px;color:var(--text);margin:8px 18px 0}

.tcard{position:absolute;top:2721px;width:409px;height:232px;background:var(--white);border-radius:28px;box-shadow:0 3px 10px rgba(0,0,0,.2)}
.tcard .face{position:absolute;left:-52px;top:56px;width:116px;height:116px;border-radius:50%;background:linear-gradient(135deg,#b8c2cc,#5d6670)}
.tcard .q{position:absolute;left:100px;top:22px;font-size:64px;font-weight:700;color:var(--blue-deep);line-height:1}
.tcard p{position:absolute;left:100px;top:78px;width:290px;font-size:13px;line-height:24px;color:var(--text);text-align:justify}
.tcard h4{position:absolute;left:100px;top:160px;font-size:16px;font-weight:500}
.tcard .stars{position:absolute;left:100px;top:182px;color:var(--star);font-size:18px;letter-spacing:2px}
.arrow{position:absolute;top:2818px;width:14px;height:14px;border-left:3px solid #777;border-bottom:3px solid #777}

.res{position:absolute;top:3197px;width:308px;height:453px;background:var(--white);box-shadow:0 2px 12px rgba(0,0,0,.12)}
.res .ph{height:207px}
.res .date{margin:22px 20px 0;font-size:13px;color:#999}
.res h3{margin:8px 20px 0;font-size:16px;font-weight:500;line-height:24px}
.res p{margin:14px 20px 0;font-size:14px;line-height:24px;color:var(--text);text-align:justify}
.res .rm{position:static;margin:16px 20px 0}

.cta h2{position:absolute;left:0;top:3862px;width:1200px;text-align:center;font-size:34px;font-weight:500;color:var(--white)}
.cta p{position:absolute;left:170px;top:3922px;width:860px;text-align:center;font-size:14px;line-height:24px;color:var(--white)}
.cta .btn{position:absolute;left:491px;top:3999px;width:220px;height:52px;background:var(--white);color:var(--blue-deep);font-size:15px}

.footer .brand{left:118px;top:4240px;font-size:30px}
.socials{position:absolute;left:160px;top:4318px;display:flex;gap:8px}
.socials i{width:28px;height:28px;border:1.5px solid #333;border-radius:50%;display:block}
.fcol{position:absolute;top:4190px}
.fcol h4{font-size:16px;font-weight:500;margin-bottom:18px}
.fcol li{list-style:none;font-size:13px;color:#555;line-height:27px}
.contact{font-size:13px;color:#555;line-height:19px;position:relative;padding-left:23px;margin-bottom:14px}
.contact b{display:block;font-size:12px;color:#222;font-weight:500}
.contact svg{position:absolute;left:0;top:2px}
.fline{position:absolute;left:110px;top:4421px;width:980px;height:1px;background:#ddd}
.copy{position:absolute;left:0;top:4448px;width:1200px;text-align:center;font-size:14px;color:#444}
.chat{position:absolute;left:1116px;top:4335px;width:40px;height:40px;border-radius:50%;background:var(--blue-deep)}
</style>
</head>
<body>

<div class="topbar">
  <span style="left:739px">Contact us</span>
  <span style="left:829px">(555) 014-2290 ⌄</span>
  <span style="left:965px">Support</span>
  <span style="left:1037px">🔒 Login</span>
</div>

<header class="nav">
  <a class="brand" href="#"><i></i>Tavrin Telecom</a>
  <nav class="menu">
    <a class="active" href="#">Home</a><a href="#">About Us</a><a href="#">Our Services</a><a href="#">Why Us?</a><a href="#">Resources</a><a href="#">Partners</a>
  </nav>
  <a class="btn btn-nav" href="#">Get started</a>
</header>

<section class="hero">
  <svg class="abs" style="left:0;top:0" width="1200" height="604" viewBox="0 0 1200 604">
    <defs>
      <linearGradient id="heroBg" x1="0" y1="0" x2="1" y2="1"><stop offset="0" stop-color="#eef4fa"/><stop offset="1" stop-color="#dbe8f4"/></linearGradient>
      <linearGradient id="city" x1="0" y1="0" x2="0" y2="1"><stop offset="0" stop-color="#c9d6e2"/><stop offset=".45" stop-color="#8d9aa6"/><stop offset="1" stop-color="#4d5258"/></linearGradient>
    </defs>
    <rect width="1200" height="604" fill="url(#heroBg)"/>
    <polygon role="img" aria-label="Hero artwork: telecom tower with antennas over a city skyline" points="470,604 1030,20 1200,0 1200,604" fill="url(#city)"/>
  </svg>
  <h1>A green, cost-effective<br>telecom network solution.</h1>
  <p>Lorem ipsum dolor sit amet, consectetur adipiscing elit, sed do incididunt ut labore et dolore magna aliqua.</p>
  <a class="btn" href="#">GET STARTED <span class="dot"></span></a>
</section>

<h2 class="h2" style="top:795px">Our Services</h2>

<div class="svc" style="left:112px;top:888px"><div class="ic"><svg width="90" height="90"><rect x="30" y="24" width="30" height="40" rx="5" fill="none" stroke="#fff" stroke-width="2.5"/><path d="M37 36h16M37 43h16M37 50h10" stroke="#fff" stroke-width="2"/></svg></div><h3>Business SMS</h3><p>Lorem ipsum dolor sit amet, consectetur adipiscing elit, sed do eiusmod tempor incididunt ut labore et dolore magna ad minim aliqua.</p><a class="more" href="#">LEARN MORE <i></i></a></div>
<div class="svc" style="left:627px;top:888px"><div class="ic"><svg width="90" height="90"><rect x="33" y="22" width="24" height="44" rx="4" fill="none" stroke="#fff" stroke-width="2.5"/><circle cx="45" cy="59" r="2" fill="#fff"/></svg></div><h3>Mobile Apps</h3><p>Lorem ipsum dolor sit amet, consectetur adipiscing elit, sed do eiusmod tempor incididunt ut labore et dolore magna ad minim aliqua.</p><a class="more" href="#">LEARN MORE <i></i></a></div>
<div class="svc" style="left:112px;top:1066px"><div class="ic"><svg width="90" height="90"><rect x="26" y="34" width="38" height="30" rx="3" fill="none" stroke="#fff" stroke-width="2.5"/><rect x="34" y="22" width="22" height="12" fill="none" stroke="#fff" stroke-width="2"/><path d="M33 44h6M43 44h6M33 52h6M43 52h6" stroke="#fff" stroke-width="2"/></svg></div><h3>Faxing</h3><p>Lorem ipsum dolor sit amet, consectetur adipiscing elit, sed do eiusmod tempor incididunt ut labore et dolore magna ad minim aliqua.</p><a class="more" href="#">LEARN MORE <i></i></a></div>
<div class="svc" style="left:627px;top:1066px"><div class="ic"><svg width="90" height="90"><rect x="24" y="26" width="42" height="28" rx="3" fill="none" stroke="#fff" stroke-width="2.5"/><circle cx="35" cy="62" r="4" fill="none" stroke="#fff" stroke-width="2"/><circle cx="55" cy="62" r="4" fill="none" stroke="#fff" stroke-width="2"/></svg></div><h3>Video Conferencing</h3><p>Lorem ipsum dolor sit amet, consectetur adipiscing elit, sed do eiusmod tempor incididunt ut labore et dolore magna ad minim aliqua.</p><a class="more" href="#">LEARN MORE <i></i></a></div>
<div class="svc" style="left:112px;top:1244px"><div class="ic"><svg width="90" height="90"><path d="M30 30c4-4 8-2 10 3l-4 5c2 5 6 9 11 11l5-4c5 2 7 6 3 10-8 6-30-12-25-25z" fill="none" stroke="#fff" stroke-width="2.5"/></svg></div><h3>Audio Conferencing</h3><p>Lorem ipsum dolor sit amet, consectetur adipiscing elit, sed do eiusmod tempor incididunt ut labore et dolore magna ad minim aliqua.</p><a class="more" href="#">LEARN MORE <i></i></a></div>
<div class="svc" style="left:627px;top:1244px"><div class="ic"><svg width="90" height="90"><rect x="24" y="24" width="16" height="12" fill="none" stroke="#fff" stroke-width="2"/><rect x="50" y="24" width="16" height="12" fill="none" stroke="#fff" stroke-width="2"/><rect x="37" y="54" width="16" height="12" fill="none" stroke="#fff" stroke-width="2"/><path d="M32 36v10h26V36M45 46v8" stroke="#fff" stroke-width="2" fill="none"/></svg></div><h3>Managed Network Service</h3><p>Lorem ipsum dolor sit amet, consectetur adipiscing elit, sed do eiusmod tempor incididunt ut labore et dolore magna ad minim aliqua.</p><a class="more" href="#">LEARN MORE <i></i></a></div>

<svg class="abs" style="left:0;top:1439px" width="1200" height="610" viewBox="0 0 1200 610">
  <defs><linearGradient id="sky" x1="0" y1="0" x2="1" y2="1"><stop offset="0" stop-color="#4f7fb8"/><stop offset=".6" stop-color="#8fb3d8"/><stop offset="1" stop-color="#c4d8ec"/></linearGradient></defs>
  <polygon points="0,120 1200,0 1200,610 0,500" fill="var(--blue-pale)"/>
  <polygon role="img" aria-label="About artwork: red and white telecom towers against a blue sky" points="0,100 795,42 420,550 0,510" fill="url(#sky)"/>
</svg>
<div class="about-txt">
  <h2>About Us</h2>
  <p>Lorem ipsum dolor sit amet, consectetur adipiscing elit, sed do eiusmod tempor incididunt ut labore et dolore magna aliqua. Ut enim ad minim veniam, quis nostrud exercitation ullamco laboris nisi ut aliquip ex ea commodo consequat.</p>
  <p>Duis aute irure dolor in reprehenderit in voluptate velit esse cillum dolore eu fugiat nulla pariatur. Excepteur sint occaecat cupidatat non proident, sunt in culpa qui officia deserunt mollit sed quia eos qui ratione voluptatem anim id est laborum.</p>
  <a class="btn" href="#">LEARN MORE <span class="dot"></span></a>
</div>

<h2 class="h2" style="top:2076px">Why Choose Us?</h2>
<div class="why" style="left:112px"><svg width="60" height="60"><circle cx="28" cy="30" r="22" fill="none" stroke="var(--blue-deep)" stroke-width="3"/><path d="M6 30h44M28 8v44M14 16c8 8 20 8 28 0M14 44c8-8 20-8 28 0" stroke="var(--blue-deep)" stroke-width="2" fill="none"/></svg><h3>Global Reliability</h3><p>Lorem ipsum dolor sit amet, consectetur adipiscing elit, do eiusmod tempor incididunt ut et dolore magna aliqua.</p></div>
<div class="why" style="left:361px"><svg width="60" height="60"><circle cx="30" cy="22" r="12" fill="var(--blue-deep)"/><path d="M8 58c0-14 10-20 22-20s22 6 22 20z" fill="var(--blue-deep)"/><path d="M16 22c0-10 6-16 14-16s14 6 14 16" stroke="var(--blue-deep)" stroke-width="3" fill="none"/></svg><h3>Customer Service</h3><p>Lorem ipsum dolor sit amet, consectetur adipiscing elit, do eiusmod tempor incididunt ut et dolore magna aliqua.</p></div>
<div class="why" style="left:609px"><svg width="60" height="60"><path d="M30 4l22 8v16c0 14-10 24-22 28C18 52 8 42 8 28V12z" fill="var(--blue-deep)"/><circle cx="30" cy="30" r="12" fill="none" stroke="#fff" stroke-width="2.5"/><path d="M24 30l4 4 8-8" stroke="#fff" stroke-width="3" fill="none"/></svg><h3>Security</h3><p>Lorem ipsum dolor sit amet, consectetur adipiscing elit, do eiusmod tempor incididunt ut et dolore magna aliqua.</p></div>
<div class="why" style="left:857px"><svg width="60" height="60"><circle cx="30" cy="16" r="11" fill="none" stroke="var(--blue-deep)" stroke-width="3"/><text x="30" y="21" font-size="14" font-weight="700" text-anchor="middle" fill="var(--blue-deep)" font-family="Roboto,sans-serif">$</text><path d="M4 32l12 20h10M56 32l-12 20H34" stroke="var(--blue-deep)" stroke-width="4" fill="none"/></svg><h3>Cost Savings</h3><p>Lorem ipsum dolor sit amet, consectetur adipiscing elit, do eiusmod tempor incididunt ut et dolore magna aliqua.</p></div>

<svg class="abs" style="left:0;top:2511px" width="1200" height="593" viewBox="0 0 1200 593"><polygon points="0,100 1200,0 1200,593 0,495" fill="var(--blue-pale)"/></svg>
<h2 class="h2" style="top:2634px">When you know us, you love us</h2>
<div class="arrow" style="left:46px;transform:rotate(45deg)"></div>
<div class="arrow" style="left:1134px;transform:rotate(-135deg)"></div>
<div class="tcard" style="left:167px"><div class="face" role="img" aria-label="Portrait of a smiling client"></div><div class="q">“</div><p>Lorem ipsum dolor sit amet, adipiscing elit, sed do eiusmod tempor incididunt ut labore et dolore magna enim ad minim aliqua.</p><h4>Marcus Hale</h4><div class="stars">★★★★★</div></div>
<div class="tcard" style="left:678px"><div class="face" role="img" aria-label="Portrait of a client in a suit"></div><div class="q">“</div><p>Lorem ipsum dolor sit amet, adipiscing elit, sed do eiusmod tempor incididunt ut labore et dolore magna enim ad minim aliqua.</p><h4>Daniel Ortiz</h4><div class="stars">★★★★★</div></div>

<h2 class="h2" style="top:3120px">Recent Resources</h2>
<div class="res" style="left:112px"><div class="ph" role="img" aria-label="Cell tower above a city at dusk" style="background:linear-gradient(180deg,#7fa3c9,#3d5e86 60%,#1f2c40)"></div><div class="date">▦ October 21, 2021</div><h3>Lorem ipsum dolor sit consectetur adipiscing elit, sed do</h3><p>Sed ut perspiciatis unde omnis iste natus sit voluptatem accusantium doloremque laudantium, totam rem aperiam,</p><a class="more rm" href="#">READ MORE <i></i></a></div>
<div class="res" style="left:446px"><div class="ph" role="img" aria-label="Engineers working in a server room" style="background:linear-gradient(135deg,#2b3a4e,#6b7f96 50%,#1a2230)"></div><div class="date">▦ October 21, 2021</div><h3>Lorem ipsum dolor sit consectetur adipiscing elit, sed do</h3><p>Sed ut perspiciatis unde omnis iste natus sit voluptatem accusantium doloremque laudantium, totam rem aperiam,</p><a class="more rm" href="#">READ MORE <i></i></a></div>
<div class="res" style="left:780px"><div class="ph" role="img" aria-label="Antenna towers at sunset over buildings" style="background:linear-gradient(180deg,#3e4452,#c7813d 55%,#2a2622)"></div><div class="date">▦ October 21, 2021</div><h3>Lorem ipsum dolor sit consectetur adipiscing elit, sed do</h3><p>Sed ut perspiciatis unde omnis iste natus sit voluptatem accusantium doloremque laudantium, totam rem aperiam,</p><a class="more rm" href="#">READ MORE <i></i></a></div>

<section class="cta">
  <svg class="abs" style="left:0;top:3732px" width="1200" height="427" viewBox="0 0 1200 427"><polygon points="0,100 1200,0 1200,427 0,330" fill="var(--blue-deep)"/></svg>
  <h2>See Tavrin in Action. Start Your Free Trial</h2>
  <p>Sed ut perspiciatis unde omnis iste natus error sit voluptatem accusantium doloremque laudantium, totam rem aperiam, eaque ipsa quae ab illo inventore veritatis et quasi architecto beatae vitae dicta sunt explicabo.</p>
  <a class="btn" href="#">START YOUR FREE TRIAL</a>
</section>

<footer class="footer">
  <div class="brand abs"><i></i>Tavrin Telecom</div>
  <div class="socials"><i></i><i></i><i></i><i></i></div>
  <div class="fcol" style="left:442px"><h4>Services</h4><ul><li>Home</li><li>About Us</li><li>Our Services</li><li>Why Us?</li><li>Resources</li><li>Partners</li></ul></div>
  <div class="fcol" style="left:636px"><h4>About Company</h4><ul><li>Privacy Policy</li><li>Terms of Service</li><li>Site Map</li><li>Imprint</li><li>Terms And Conditions</li></ul></div>
  <div class="fcol" style="left:873px"><h4>Contact Us</h4>
    <div class="contact"><svg width="14" height="14"><path d="M2 2c2-2 4-1 5 1l-2 3c1 2 3 4 5 5l3-2c2 1 2 3 0 4-5 3-14-6-11-11z" fill="var(--blue-deep)"/></svg><b>Phone</b>(555) 014-2290</div>
    <div class="contact"><svg width="14" height="12"><rect width="14" height="11" rx="1" fill="var(--blue-deep)"/><path d="M1 1l6 5 6-5" stroke="#fff" fill="none"/></svg><b>Email</b>hello@tavrintelecom.example</div>
    <div class="contact"><svg width="12" height="16"><path d="M6 0a6 6 0 0 1 6 6c0 4-6 10-6 10S0 10 0 6a6 6 0 0 1 6-6z" fill="var(--blue-deep)"/><circle cx="6" cy="6" r="2" fill="#fff"/></svg><b>Location</b>81 Lorem ipsum dolor sit amet,<br>consectetur adipiscing elit,</div>
  </div>
  <div class="chat"></div>
  <div class="fline"></div>
  <div class="copy">2022 Copyright - &nbsp;tavrintelecom &nbsp;| All Rights Reserved</div>
</footer>

</body>
</html>
```